Design a Banner for my solo ads page

Hey guys,

I need a simple banner designed for my solo ads page. It needs to be about 900 x 250px

I will supply a photo but I was thinking of adding some different effects to it as I want it to stand out on the top of the page (Do something creative with this the resolution isn't the best but Its kind of a funny image to warm people. It needs to be on the left though. I might decide to change this so please send me the psd and the ability to do this easily.)

We can skype after to chat about future work too :)

Must be willing to work with me on this and have decent design skills

I need a copy of this in both psd and png format.

Headline: Colin Pereira's
Sub: Velvet Solo Ads

Cheers guys,

-Colin

```html
<!DOCTYPE html>
<html lang="en">
<head>
<meta charset="utf-8">
<title>Colin Pereira's Velvet Solo Ads</title>
<link rel="stylesheet" href="https://fonts.googleapis.com/css2?family=Source+Sans+3:ital,wght@0,600;1,600&display=swap">
<style>
  :root {
    --cream-light: #f7f3d6;
    --cream: #ece6b4;
    --cream-deep: #d9d29a;
    --swirl: #cfc58e;
    --headline: #7b2a3d;
    --headline-shadow: rgba(70, 30, 20, 0.35);
    --sub: #4a4636;
    --photo-skin: #c99a7f;
    --photo-dark: #1d1a18;
    --photo-wall: #e7e1c9;
    --streak-gold: #f2d57a;
    --streak-green: #b9d6a3;
    --streak-blue: #a9cde0;
    --streak-rose: #e8b7a8;
  }
  html, body {
    margin: 0;
    padding: 0;
    width: 1200px;
    height: 333px;
    overflow: hidden;
    background: #ffffff;
  }
  .banner {
    position: relative;
    width: 1200px;
    height: 333px;
    overflow: hidden;
    background: linear-gradient(100deg, var(--cream-deep) 0%, var(--cream) 35%, var(--cream-light) 75%, #fbf9ec 100%);
  }
  .banner__backdrop {
    position: absolute;
    inset: 0;
  }
  .banner__portrait {
    position: absolute;
    left: 0;
    top: 0;
    width: 340px;
    height: 333px;
    background:
      radial-gradient(ellipse 95px 125px at 185px 140px, var(--photo-skin) 0%, var(--photo-skin) 60%, rgba(201,154,127,0) 100%),
      linear-gradient(180deg, var(--photo-wall) 0%, var(--photo-wall) 55%, var(--photo-dark) 72%, var(--photo-dark) 100%);
    -webkit-mask-image: linear-gradient(90deg, #000 70%, transparent 100%);
            mask-image: linear-gradient(90deg, #000 70%, transparent 100%);
  }
  .banner__title {
    position: absolute;
    left: 287px;
    top: 14px;
    margin: 0;
    font-family: "Source Sans 3", "Myriad Pro", sans-serif;
    font-weight: 600;
    font-size: 68px;
    line-height: 1;
    letter-spacing: 1px;
    color: var(--headline);
    text-shadow: 2px 3px 4px var(--headline-shadow);
  }
  .banner__subtitle {
    position: absolute;
    left: 377px;
    top: 86px;
    margin: 0;
    font-family: "Source Sans 3", "Myriad Pro", sans-serif;
    font-style: italic;
    font-weight: 600;
    font-size: 20px;
    line-height: 1;
    letter-spacing: 2.5px;
    color: var(--sub);
  }
</style>
</head>
<body>
  <div class="banner">
    <svg class="banner__backdrop" width="1200" height="333" viewBox="0 0 1200 333" aria-hidden="true">
      <defs>
        <linearGradient id="streaks" x1="0" y1="1" x2="1" y2="0">
          <stop offset="0" stop-color="var(--streak-rose)" stop-opacity="0.3"/>
          <stop offset="0.3" stop-color="var(--streak-gold)" stop-opacity="0.55"/>
          <stop offset="0.55" stop-color="var(--streak-green)" stop-opacity="0.5"/>
          <stop offset="0.8" stop-color="var(--streak-blue)" stop-opacity="0.45"/>
          <stop offset="1" stop-color="#ffffff" stop-opacity="0.6"/>
        </linearGradient>
        <linearGradient id="streakFade" x1="0" y1="0" x2="1" y2="0">
          <stop offset="0" stop-color="#fff" stop-opacity="0"/>
          <stop offset="0.45" stop-color="#fff" stop-opacity="1"/>
          <stop offset="1" stop-color="#fff" stop-opacity="1"/>
        </linearGradient>
        <mask id="streakMask" maskUnits="userSpaceOnUse" x="560" y="0" width="640" height="333">
          <rect x="560" y="0" width="640" height="333" fill="url(#streakFade)"/>
        </mask>
        <radialGradient id="swirlGlow" cx="0.5" cy="0.5" r="0.5">
          <stop offset="0" stop-color="var(--swirl)" stop-opacity="0.45"/>
          <stop offset="1" stop-color="var(--swirl)" stop-opacity="0"/>
        </radialGradient>
      </defs>
      <rect class="backdrop__swirl-area" x="240" y="0" width="520" height="333" fill="url(#swirlGlow)" role="img" aria-label="Faint decorative swirl pattern"/>
      <rect class="backdrop__light-streaks" x="560" y="0" width="640" height="333" fill="url(#streaks)" mask="url(#streakMask)" role="img" aria-label="Soft rainbow light streaks"/>
    </svg>

    <div class="banner__portrait" role="img" aria-label="Photo of Colin smiling"></div>

    <h1 class="banner__title">Colin Pereira's</h1>
    <p class="banner__subtitle">Velvet Solo Ads</p>
  </div>
</body>
</html>
```